Design a large parking banner – mandatory ticket validation in the shop

Banner Size:
548 cm (width) x 154 cm (height)
Note: The banner will be placed in a metal frame at our parking lot entrance, fully visible to every incoming truck driver. The message must be easy to read from a distance.
Goal of the Banner:
To inform all truck drivers that they must validate their entry ticket inside the shop, even if they are parking for a short time.
The message must be displayed in multiple languages for international drivers.
Mandatory Content:
Main message – in multiple languages (clearly separated or stacked):
Dutch (NL): Vergeet je ticket niet te valideren in de shop – verplicht, ook bij kort parkeren!
French (FR): N'oubliez pas de valider votre ticket à la boutique – obligatoire, même pour un court arrêt !
English (EN): Don't forget to validate your entry ticket in the shop – mandatory, even for short stops!
German (DE): Vergessen Sie nicht, Ihr Einfahrticket im Shop zu entwerten – Pflicht, auch bei kurzem Parken!
Polish (PL): Nie zapomnij zatwierdzić biletu w sklepie – obowiązkowe, nawet przy krótkim postoju!
Romanian (RO): Nu uitați să validați biletul în magazin – obligatoriu, chiar și pentru opriri scurte!
You can include more languages if space allows, but these are essential.
Opening Hours Block (in one section below):
Shop Opening Hours
Mon – Fri: 05:30 – 22:00
Sat & Sun: 08:00 – 22:00
Style & Branding:
The design must match the visual identity of Haulpoint 41Ter
Please refer to the attached photos of existing parking signage for guidance on colors, typography, and layout style
Our logo (attached) must be clearly visible and professionally integrated
Feel free to use icons or pictograms to visually support the message (e.g., ticket, truck, arrow)
Readability is key – large, bold text and high contrast colors that are visible from a distance
Target Audience:
International truck drivers – people who need fast, clear communication. Not everyone speaks the local language, so visual clarity and multilingual messaging are critical.
File Requirements:
Print-ready file (PDF or EPS) – 300 dpi at 1:10 scale
Include 5 cm bleed on all sides
Provide open source files if possible (AI or PSD)

```html
<!DOCTYPE html>
<html lang="en">
<head>
<meta charset="utf-8">
<title>Haulpoint 41Ter – Ticket validation banner</title>
<link rel="stylesheet" href="https://fonts.googleapis.com/css2?family=Bebas+Neue&family=Poppins:wght@600;700&display=swap">
<style>
  :root {
    --navy: #1f2a5e;
    --red: #d0202a;
    --blue: #1c7fd1;
    --white: #ffffff;
    --backdrop: #e6e5e6;
  }
  html, body {
    margin: 0;
    width: 1200px;
    height: 436px;
    overflow: hidden;
    background: var(--backdrop);
  }
  .stage {
    position: relative;
    width: 1200px;
    height: 436px;
  }
  .banner {
    position: absolute;
    left: 40px;
    top: 61px;
    width: 1319px;
    height: 370px;
    background: var(--white);
    transform: scale(0.8491);
    transform-origin: top left;
    overflow: hidden;
  }
  .banner-shapes {
    position: absolute;
    inset: 0;
  }
  .brand-name {
    position: absolute;
    left: 42px;
    top: 30px;
    margin: 0;
    font-family: "Bebas Neue", sans-serif;
    font-weight: 400;
    font-size: 66px;
    line-height: 0.92;
    color: var(--navy);
    letter-spacing: 1px;
  }
  .hours {
    position: absolute;
    left: 37px;
    top: 174px;
    width: 280px;
    font-family: "Poppins", sans-serif;
  }
  .hours-title {
    margin: 0 0 6px;
    font-size: 22.5px;
    font-weight: 700;
    color: var(--blue);
    white-space: nowrap;
  }
  .hours-row {
    display: flex;
    align-items: flex-start;
    padding: 3px 0 4px;
  }
  .hours-row + .hours-row {
    border-top: 1px solid rgba(255,255,255,0.35);
    padding-top: 6px;
  }
  .hours-day {
    width: 115px;
    font-size: 24.5px;
    font-weight: 600;
    line-height: 1.02;
    color: var(--white);
  }
  .hours-time {
    font-size: 27px;
    font-weight: 600;
    line-height: 1.02;
    color: var(--red);
    letter-spacing: 0.5px;
    white-space: nowrap;
  }
  .message {
    position: absolute;
    margin: 0;
    height: 28px;
    line-height: 29px;
    font-family: "Bebas Neue", sans-serif;
    font-style: italic;
    font-size: 25.5px;
    white-space: nowrap;
    color: var(--navy);
  }
  .message-lead { color: var(--blue); }
  .lang-label {
    position: absolute;
    width: 110px;
    height: 28px;
    line-height: 30px;
    text-align: center;
    font-family: "Bebas Neue", sans-serif;
    font-style: italic;
    font-size: 19.5px;
    color: var(--white);
    letter-spacing: 0.3px;
    white-space: nowrap;
  }
</style>
</head>
<body>
<div class="stage">
  <section class="banner" aria-label="Ticket validation banner">
    <svg class="banner-shapes" width="1319" height="370" viewBox="0 0 1319 370" aria-hidden="true">
      <polygon class="hours-panel" fill="#1f2a5e" points="395,0 408,0 283,370 0,370 0,163 340,163"/>
      <polygon class="accent-stripe" fill="#d0202a" points="408,0 420,0 295,370 283,370"/>
      <g class="lang-tabs" fill="#d0202a">
        <polygon points="404,41 537,41 528,69 395,69"/>
        <polygon points="386,93 520,93 511,121 377,121"/>
        <polygon points="369,145 504,145 495,173 360,173"/>
        <polygon points="351,197 488,197 479,225 342,225"/>
        <polygon points="334,249 470,249 461,277 325,277"/>
        <polygon points="316,301 454,301 445,329 307,329"/>
      </g>
    </svg>

    <h1 class="brand-name">Haulpoint<br>41Ter</h1>

    <div class="hours">
      <h2 class="hours-title">SHOP OPENING HOURS</h2>
      <div class="hours-row">
        <span class="hours-day">MON TO<br>FRIDAY</span>
        <span class="hours-time">05:30 TO<br>22:00</span>
      </div>
      <div class="hours-row">
        <span class="hours-day">SAT &amp;<br>SUN</span>
        <span class="hours-time">08:00 TO<br>22:00</span>
      </div>
    </div>

    <span class="lang-label" style="left:410px;top:41px">DUTCH (NL)</span>
    <p class="message" style="left:539px;top:41px"><span class="message-lead">VERGEET JE TICKET NIET TE VALIDEREN IN DE SHOP —</span> VERPLICHT, OOK BIJ KORT PARKEREN!</p>

    <span class="lang-label" style="left:393px;top:93px">FRENCH (FR)</span>
    <p class="message" style="left:522px;top:93px"><span class="message-lead">N'OUBLIEZ PAS DE VALIDER VOTRE TICKET À LA BOUTIQUE —</span> OBLIGATOIRE, MÊME POUR UN COURT ARRÊT !</p>

    <span class="lang-label" style="left:377px;top:145px">ENGLISH (EN)</span>
    <p class="message" style="left:506px;top:145px"><span class="message-lead">DON'T FORGET TO VALIDATE YOUR ENTRY TICKET IN THE SHOP —</span> MANDATORY, EVEN FOR SHORT STOPS!</p>

    <span class="lang-label" style="left:360px;top:197px">GERMAN (DE)</span>
    <p class="message" style="left:490px;top:197px"><span class="message-lead">VERGESSEN SIE NICHT, IHR EINFAHRTICKET IM SHOP ZU ENTWERTEN —</span> PFLICHT, AUCH BEI KURZEM PARKEN!</p>

    <span class="lang-label" style="left:342px;top:249px">POLISH (PL)</span>
    <p class="message" style="left:472px;top:249px"><span class="message-lead">NIE ZAPOMNIJ ZATWIERDZIĆ BILETU W SKLEPIE —</span> OBOWIĄZKOWE, NAWET PRZY KRÓTKIM POSTOJU!</p>

    <span class="lang-label" style="left:325px;top:301px">ROMANIAN (RO)</span>
    <p class="message" style="left:456px;top:301px"><span class="message-lead">NU UITAȚI SĂ VALIDAȚI BILETUL ÎN MAGAZIN —</span> OBLIGATORIU, CHIAR ȘI PENTRU OPRIRI SCURTE!</p>
  </section>
</div>
</body>
</html>
```